Verantis Guest Event Collateral

Create a double-sided, oversized piece of collateral for a series of guest networking events that we'll be hosting in 2019

We are looking for this piece of collateral to be the size of an oversized post card (1/2 of an 8/5 x 11 piece of paper). The front should include the following: Verantis's Mission Statement: Continually foster a culture of community and education for focused business professionals. How do we do it? Using four distinct principles, Verantis offers business professionals the opportunity to be successful right now ,as well as next year. Through in-person meetings, virtual meetings, networking events, and educational opportunities Verantis offers members a chance to hit their goals not only this year, but every year! Collaboration: Work with like-minded, driven Verantis members to collaborate and overcome the objections, hurdles and challenges that all business professionals face, either in person at twice monthly meetings, or virtually, from the comfort of your home or office. Accountability: Stay on track, and complete the goals you have set for yourself! Weekly in person or virtual meetings afford all members the opportunity to review their plan twice a month with fellow Verantis members, and trained Verantis coaches. Referrals: In the midst of crafting an executable, measurable and attainable plan let Verantis build your business through a steady stream of referrals via six yearly networking events, specifically designed to ensure you walk away with new referral partners. Strategy: Let Verantis assist you in crafting a strategy within our proven business planning template; realistic, understandable, measurable, beyond normal, attainable and time bound. The back should include the following: Become a Verantis member for $150/month and join us for 6 Networking Events in 2019 plus much more! We aren’t just about collaboration, accountability and strategy! Creating opportunities for referrals is also a cornerstone of Verantis! To make certain we are delivering on this principle, Verantis will host 6 events throughout 2019, complete with specific activities at each event to ensure you meet everyone in the room, making immediate connects to build your referral network. Join now and put yourself in position for success in 2019! Name: Phone: Email: Company Name: Industry: Position: Credit Card Number: Exp. Date: Testimonials: Overall I think people are lazy. I know I am! The benefits I have found and have come to truly appreciate thru Verantis are a sense of professionalism, accountability and shared enthusiasm. These things break that cycle of laziness for me and, I am sure, many others. When I walk into a meeting I know that positive and helpful feedback is the name of the game. Feedback from others and in many other industries from my own has become a key and cornerstone to my business and personal success. I would urge anyone no matter what your occupation to attend a couple of meetings and see how this group of like minded professionals can help you to achieve more. More time, More success, More health, More security, More money, More happiness..............What could you use more of? Gordon T. Melby Sr. Automotive Consultant Ridgewater Leasing & Sales Thank you!

Target Market(s)

Small business owners, entrpreneurs, networkers, sales people

Industry/Entity Type

Business Consultant

Font styles to use
Sans Serif

Colors
f36f22
f68d4e
f8ba93
f78f20
faa54b

Requirements
Must have
• - Imagery
• - Our company logo
• - Clear CTA to check out our website (www.verantis-example.com)
• - Option to "Join the Verantis Community Today!" and include a spot for someone to fill in their name, email address, company name, and phone number
• - Reference that we host 6+ networking events in Denver throughout the year that are free to attend and are unlike any other networking event they've attended before
• - Mention that we have in-person meetings 2x per month, virtual meeting options, networking events, and educational events
• - Highlight the following acronym which references our core company components:
• Collaboration:
• Work with like-minded, driven Verantis members to collaborate and overcome the objections, hurdles and challenges that all business professionals face, in either in person twice monthly meetings, or virtually, from the comfort of your home of office.
• Accountability:
• Stay on track, and complete the goals you have set for yourself! Weekly in person or virtual meetings afford all members the opportunity to review their plan twice a month with your fellow Verantis members and trained Verantis coaches, to make certain you success is continuous throughout the year.
• Referrals:
• In the midst of crafting an executable, measurable and attainable plan let Verantis build your business through a steady stream of referral opportunities via twelve yearly networking events, specifically designed to ensure you walk away with new referral partners.
• Strategy:
• Let Verantis assist you in crafting a strategy within our proven business planning template; realistic, understandable, measurable, beyond normal, attainable and time bound.

```html
<!DOCTYPE html>
<html lang="en">
<head>
<meta charset="utf-8">
<title>Verantis Guest Event Collateral</title>
<link href="https://fonts.googleapis.com/css2?family=Montserrat:wght@400;700;800&family=Open+Sans:wght@400;600&display=swap" rel="stylesheet">
<style>
  :root{
    --orange:#f07f1e;
    --orange-dark:#d96a12;
    --slate:#3d4954;
    --ink:#1f2328;
    --muted:#4a4f55;
    --paper:#ffffff;
    --backdrop:#e9e7e4;
    --field:#f7f8fa;
  }
  *{box-sizing:border-box;margin:0;padding:0}
  html,body{width:1200px;height:801px;overflow:hidden;background:var(--backdrop)}
  body{position:relative;font-family:"Open Sans",sans-serif;color:var(--ink)}
  .page{position:absolute;top:30px;width:535px;height:740px;background:var(--paper);overflow:hidden;box-shadow:0 6px 18px rgba(0,0,0,.18)}
  .page--front{left:45px}
  .page--back{left:620px}
  .art{position:absolute;left:0;top:0}
  .brand{position:absolute;left:36px;top:40px;display:flex;align-items:center;gap:8px;font-family:"Montserrat",sans-serif;font-weight:400;font-size:24px;color:var(--slate);letter-spacing:.5px}
  .brand__mark{width:22px;height:22px;background:var(--orange)}
  .event-title{position:absolute;left:72px;top:288px;font-family:"Montserrat",sans-serif;font-weight:800;color:#fff;line-height:1}
  .event-title__small{display:block;font-size:22px}
  .event-title__big{display:block;font-size:40px;margin-top:6px}
  .intro{position:absolute;left:40px;top:400px;width:300px;font-size:10px;line-height:1.45;color:var(--muted)}
  .intro p+p{margin-top:8px}
  .join{position:absolute;left:40px;top:494px;font-family:"Montserrat",sans-serif;font-weight:700;font-size:19px;color:var(--ink)}
  .field{position:absolute;width:220px}
  .field__label{font-size:12px;text-transform:uppercase;color:var(--ink);margin-bottom:5px}
  .field__box{height:38px;border:1.5px solid var(--ink);background:var(--field)}
  .f-name{left:40px;top:532px}
  .f-company{left:290px;top:520px}
  .f-email{left:40px;top:600px}
  .f-phone{left:290px;top:588px}
  .footer{position:absolute;left:0;bottom:0;width:100%}
  .footer__band{height:52px;background:var(--orange);display:flex;align-items:center;justify-content:center;font-size:12px;color:var(--ink)}
  .footer__base{height:14px;background:var(--slate)}
  .components-title{position:absolute;left:290px;top:170px;font-family:"Montserrat",sans-serif;font-weight:800;color:#fff;line-height:1.05}
  .components-title__big{display:block;font-size:36px}
  .components-title__small{display:block;font-size:25px;padding-left:16px}
  .pillars{position:absolute;left:36px;top:335px;width:470px;display:grid;grid-template-columns:1fr 1fr;column-gap:30px;row-gap:22px}
  .pillar h3{font-family:"Montserrat",sans-serif;font-weight:700;font-size:14px;color:var(--ink);margin-bottom:4px}
  .pillar p{font-size:9px;line-height:1.5;color:var(--muted)}
</style>
</head>
<body>

<section class="page page--front" aria-label="Front: Guest Networking Event 2019">
  <svg class="art" width="535" height="400" viewBox="0 0 535 400">
    <defs>
      <linearGradient id="eventPhoto" x1="0" y1="0" x2="1" y2="1">
        <stop offset="0" stop-color="#c9b39a"/>
        <stop offset=".45" stop-color="#7e8894"/>
        <stop offset="1" stop-color="#2d333b"/>
      </linearGradient>
    </defs>
    <polygon role="img" aria-label="Photo of a presenter speaking to a seated audience at a networking event"
      points="230,0 535,0 535,358 450,358 398,392 140,236" fill="url(#eventPhoto)"/>
    <polygon points="40,208 178,208 168,262" fill="var(--slate)"/>
    <polygon points="55,278 380,266 386,364 60,380" fill="var(--orange)"/>
    <polygon points="340,366 386,364 370,378" fill="var(--orange-dark)"/>
  </svg>

  <div class="brand"><span class="brand__mark"></span>VERANTIS</div>

  <h1 class="event-title">
    <span class="event-title__small">Guest Networking</span>
    <span class="event-title__big">Event 2019</span>
  </h1>

  <div class="intro">
    <p>we host 6+ networking events in Denver throughout the year that are free to attend and are unlike any other networking event they've attended before.</p>
    <p>we have in-person meetings 2x per month, virtual meeting options, networking events, and educational events.</p>
  </div>

  <h2 class="join">Join the Verantis Community Today!</h2>

  <div class="field f-name"><div class="field__label">Name</div><div class="field__box"></div></div>
  <div class="field f-company"><div class="field__label">Company Name</div><div class="field__box"></div></div>
  <div class="field f-email"><div class="field__label">Email Address</div><div class="field__box"></div></div>
  <div class="field f-phone"><div class="field__label">Phone Number</div><div class="field__box"></div></div>

  <footer class="footer">
    <div class="footer__band">www.verantis-example.com</div>
    <div class="footer__base"></div>
  </footer>
</section>

<section class="page page--back" aria-label="Back: Company Components">
  <svg class="art" width="535" height="330" viewBox="0 0 535 330">
    <defs>
      <linearGradient id="teamPhoto" x1="0" y1="0" x2="1" y2="1">
        <stop offset="0" stop-color="#b9b2a8"/>
        <stop offset=".5" stop-color="#6f767e"/>
        <stop offset="1" stop-color="#d9dadc"/>
      </linearGradient>
    </defs>
    <rect x="20" y="18" width="420" height="18" fill="var(--slate)"/>
    <rect x="420" y="18" width="40" height="255" fill="var(--slate)"/>
    <rect role="img" aria-label="Photo of two colleagues reviewing charts together at a desk"
      x="20" y="36" width="410" height="280" fill="url(#teamPhoto)"/>
    <rect x="270" y="152" width="265" height="108" fill="var(--orange)"/>
    <polygon points="300,260 340,260 325,282" fill="var(--orange-dark)"/>
  </svg>

  <h2 class="components-title">
    <span class="components-title__big">Company</span>
    <span class="components-title__small">Components</span>
  </h2>

  <div class="pillars">
    <article class="pillar">
      <h3>Collaboration</h3>
      <p>Work with like-minded, driven Verantis members to collaborate and overcome the objections, hurdles and challenges that all business professionals face, in either in person twice monthly meetings, or virtually, from the comfort of your home or office.</p>
    </article>
    <article class="pillar">
      <h3>Accountability</h3>
      <p>Stay on track, and complete the goals you have set for yourself! Weekly in person or virtual meetings afford all members the opportunity to review their plan twice a month with fellow Verantis members and trained Verantis coaches, to make certain your success is continuous throughout the year.</p>
    </article>
    <article class="pillar">
      <h3>Referrals</h3>
      <p>In the midst of crafting an executable, measurable and attainable plan let Verantis build your business through a steady stream of referral opportunities via twelve yearly networking events, specifically designed to ensure you walk away with new referral partners.</p>
    </article>
    <article class="pillar">
      <h3>Strategy</h3>
      <p>Let Verantis assist you in crafting a strategy within our proven business planning template; realistic, understandable, measurable, beyond normal, attainable and time bound.</p>
    </article>
  </div>

  <footer class="footer">
    <div class="footer__band">www.verantis-example.com</div>
    <div class="footer__base"></div>
  </footer>
</section>

</body>
</html>
```